KeyHarbor needs a modern business card

We are a modern conveyancing company and we need to appeal to the top (Multi-million dollar properties)and bottom on the property conveyancing market but our sweet spot is the middle of the market. I like professional with a hint of unconventional.

Target Market(s)

As above

Industry/Entity Type

Real Estate

Contact Information for Business Card

Back Of card:
thinking black with the logo and a tag line (I could be wrong about the black)
Tag line - Right Expertise, Exceptional Service

Front of Card:
Marissa Toll (BBus (Finance) LLB)
Licensed Conveyancer
Email: marissa@keyharbor.com.au

Key Harbor
ABN: 48 913 706
Suite 14, Level 3, 9 Calloway Road Lindhurst Park, NSW 2178
Phone: 1300 682 917

Sydney - Melbourne - Brisbane (Perhaps have this along the bottom of the card)

Requirements
Must have
• Sleek, modern and top end appeal (But approachable)
Should not have
• Not too cluttered

```html
<!DOCTYPE html>
<html lang="en">
<head>
<meta charset="utf-8">
<title>KeyHarbor Business Card</title>
<link href="https://fonts.googleapis.com/css2?family=Arimo:ital,wght@0,400;0,700;1,400&display=swap" rel="stylesheet">
<style>
  :root {
    --page: #e6e6e4;
    --card-dark: #231f20;
    --brand-blue: #0b4a78;
    --brand-blue-deep: #083a60;
    --accent-sky: #4cc3ee;
    --text-light: #ffffff;
  }
  * { margin: 0; padding: 0; box-sizing: border-box; }
  html, body { width: 1200px; height: 900px; overflow: hidden; }
  body {
    background: var(--page);
    font-family: "Arimo", Arial, sans-serif;
    color: var(--text-light);
    display: flex;
    flex-direction: column;
    align-items: center;
    justify-content: center;
    gap: 40px;
  }
  .card {
    position: relative;
    width: 620px;
    height: 379px;
    background: var(--card-dark);
    overflow: hidden;
    box-shadow: 0 6px 18px rgba(0,0,0,0.25);
  }
  .card svg.card-shapes { position: absolute; inset: 0; }

  /* Back of card */
  .brand-lockup {
    position: absolute;
    left: 0; right: 0;
    display: flex;
    align-items: center;
    justify-content: center;
    gap: 14px;
  }
  .brand-mark {
    width: 22px; height: 22px;
    background: var(--accent-sky);
  }
  .brand-name { font-weight: 700; color: var(--text-light); }
  .card-back .brand-lockup { top: 118px; }
  .card-back .brand-name { font-size: 44px; }
  .card-back .brand-mark { width: 30px; height: 30px; }
  .tagline-band {
    position: absolute;
    left: 0; right: 0;
    top: 215px;
    height: 46px;
    background: var(--brand-blue);
    display: flex;
    align-items: center;
    justify-content: center;
  }
  .tagline {
    font-style: italic;
    font-size: 21px;
    letter-spacing: 0.3px;
    text-transform: uppercase;
  }

  /* Front of card */
  .holder {
    position: absolute;
    left: 42px; top: 62px;
  }
  .holder-name { font-size: 26px; text-transform: uppercase; letter-spacing: 0.3px; }
  .holder-role { font-size: 15px; font-style: italic; line-height: 21px; margin-top: 6px; }
  .holder-email {
    position: absolute;
    left: 36px; top: 180px;
    display: flex; align-items: center; gap: 8px;
    font-size: 17px; font-style: italic;
  }
  .cities {
    position: absolute;
    left: 26px; top: 300px;
    font-size: 24px;
    font-style: italic;
  }
  .office {
    position: absolute;
    left: 380px; top: 60px;
    width: 220px;
  }
  .card-front .brand-lockup { position: static; justify-content: flex-start; gap: 10px; margin-bottom: 22px; }
  .card-front .brand-name { font-size: 26px; }
  .card-front .brand-mark { width: 18px; height: 18px; }
  .office-details { font-size: 16px; line-height: 22px; }
  .office-phone {
    display: flex; align-items: center; gap: 6px;
    font-size: 18px; margin-top: 8px;
  }
</style>
</head>
<body>

  <section class="card card-back" aria-label="Back of card">
    <div class="brand-lockup">
      <span class="brand-mark"></span>
      <span class="brand-name">KeyHarbor</span>
    </div>
    <div class="tagline-band">
      <p class="tagline">Right Expertise, Exceptional Service</p>
    </div>
  </section>

  <section class="card card-front" aria-label="Front of card">
    <svg class="card-shapes" width="620" height="379" viewBox="0 0 620 379" aria-hidden="true">
      <path d="M0 0 H282 C300 110 318 210 334 292 H0 Z" fill="var(--brand-blue)"/>
      <path d="M302 0 H318 C300 95 312 210 340 290 C318 220 298 110 302 0 Z" fill="var(--brand-blue)"/>
      <path d="M0 336 H332 L362 379 H0 Z" fill="var(--brand-blue)"/>
    </svg>

    <div class="holder">
      <h1 class="holder-name">Marissa Toll</h1>
      <p class="holder-role">(BBus (Finance) LLB)<br>Licensed Conveyancer</p>
    </div>

    <p class="holder-email">
      <svg width="20" height="14" viewBox="0 0 20 14" aria-hidden="true">
        <rect x="0.75" y="0.75" width="18.5" height="12.5" fill="none" stroke="#fff" stroke-width="1.5"/>
        <path d="M1 1 L10 8 L19 1 M1 13 L7.5 6 M19 13 L12.5 6" fill="none" stroke="#fff" stroke-width="1.3"/>
      </svg>
      marissa@keyharbor.com.au
    </p>

    <p class="cities">Sydney - Melbourne - Brisbane</p>

    <div class="office">
      <div class="brand-lockup">
        <span class="brand-mark"></span>
        <span class="brand-name">KeyHarbor</span>
      </div>
      <p class="office-details">
        ABN: 48 913 706<br>
        Suite 14, Level 3,<br>
        9 Calloway Road<br>
        Lindhurst Park,<br>
        NSW 2178
      </p>
      <p class="office-phone">
        <svg width="22" height="22" viewBox="0 0 22 22" aria-hidden="true">
          <circle cx="11" cy="11" r="10" fill="none" stroke="#fff" stroke-width="1.5"/>
          <path d="M7.5 5.5 L9.3 5.5 L10.2 8.3 L9 9.3 C9.7 10.8 11.2 12.3 12.7 13 L13.7 11.8 L16.5 12.7 L16.5 14.5 C16.5 15.5 15.5 16.3 14.5 16 C10.5 15 7 11.5 6 7.5 C5.7 6.5 6.5 5.5 7.5 5.5 Z" fill="#fff"/>
        </svg>
        1300 682 917
      </p>
    </div>
  </section>

</body>
</html>
```